Website Design for Solar Panel Company

We are working with a company called BrightVX.

Some sites to use for content/competitors and inspiration:
https://www.dawnmill.com
https://prod.cdn-prod.raylokt.com
https://mossbeamvolt.net
https://www.quorvin.com/solarpanels

Thank you for taking the time to consider designing a website for us. We are web developers based in Stockton, CA, USA. Most of our projects go through the same process. Understanding this process may help you win a project with us. We custom-code all of our websites in-house. We don’t have any requirements as to what tools you use for your design, but we prefer Figma files. For any design that we label as four-stars, we send it to the client for review. The client picks the final design they want us to use. Once we complete this process, we will continue to show additional clients all the four-star sites and purchase them later. Your designs will have multiple chances to sell. For better chances of success, we ask that you follow these guidelines.

IMAGES:
If you use any images or icons in the design, we ask that you have a link to the asset so we can purchase the image/icon. Most of the designs we submit do not have the customer’s images on them unless they have some great images. Be creative; show us the feeling you are trying to portray with your image choices. Use any royalty-free site you choose. We subscribe to Corvane and mainly use their images, but we can purchase images outside of Corvane. PLEASE NOTE: we will not submit designs to clients with watermarks on the images.

FONTS:
We ask that you identify the fonts used in the design. This can be done in a message if you want. We typically use Tivelo Fonts and Corvane Fonts.

CONTENT:
We're always open to different content and ideas. We often submit designs with stock images so the client can see our vision. We typically take pictures after the website launch to use their images with our vision. Lorem Ipsum is fine for paragraphs, but we ask that you write the headers in correct English. We want to be able to show the vision and identify the sections of the website.

INSPIRATION:
We typically add a couple of links in the brief of websites we like to help you get started in your design.

REVISIONS:
We do not often ask for revisions of the designs unless we see something in the design that may not appeal to the client. If there are slight changes that we want to make, we do that in the development process.

FEEDBACK:
We rarely give feedback on designs during the design process. We are working on many website projects and do not have the time to provide feedback. We usually respond if your request is well thought out and asks specific questions, but a note asking “feedback, please” usually goes unanswered.

```html
<!DOCTYPE html>
<html lang="en">
<head>
<meta charset="utf-8">
<title>BrightVX – Solar Energy</title>
<link href="https://fonts.googleapis.com/css2?family=Tinos:wght@400;700&family=Lato:wght@400;700;900&display=swap" rel="stylesheet">
<style>
:root{
  --navy:#13305f;
  --navy-dark:#0c2149;
  --green:#6cb52d;
  --green-dark:#58981f;
  --ink:#2b2f36;
  --muted:#6b7280;
  --light:#f3f4f6;
  --line:#dfe3ea;
  --white:#ffffff;
  --sky:#a9c2d8;
  --panel:#1d4f86;
  --sand:#c9a27a;
}
*{box-sizing:border-box;margin:0;padding:0}
html,body{width:1200px;height:4840px;overflow:hidden}
body{font-family:"Lato",Arial,sans-serif;color:var(--ink);background:var(--white);position:relative}
.serif{font-family:"Tinos","Times New Roman",serif}
section,header,footer{position:absolute;left:0;width:1200px}
.abs{position:absolute}
.tag{font-size:11px;font-weight:700;letter-spacing:1.5px;color:var(--green);text-transform:uppercase;display:flex;align-items:center;gap:10px}
.tag::before,.tag.center::after{content:"";width:36px;height:2px;background:var(--green)}
.btn{display:inline-block;background:var(--green);color:#fff;font-size:13px;font-weight:700;padding:14px 30px;border-radius:4px;text-decoration:none}
.ph{border-radius:0}

/* header */
.header{top:0;height:80px;background:#fff;z-index:5}
.logo{left:100px;top:14px;display:flex;align-items:center;gap:10px}
.logo .dot{width:14px;height:14px;border-radius:50%;background:var(--green)}
.logo span{font-family:"Lato",sans-serif;font-weight:900;font-size:30px;color:var(--navy);letter-spacing:.5px}
.topbar{left:330px;top:0;height:30px;display:flex;align-items:center;gap:40px;font-size:12px;color:var(--ink)}
.topbar .wel{font-weight:700;letter-spacing:1px}
.topbar .mail{display:flex;align-items:center;gap:8px}
.nav{left:320px;top:44px;display:flex;gap:0}
.nav a{font-size:13px;color:var(--ink);text-decoration:none;padding:10px 22px;font-weight:700}
.nav a.active{background:var(--green);color:#fff}
.callbox{right:0;top:0;width:330px;height:90px;background:var(--navy);color:#fff;display:flex;align-items:center;gap:14px;padding-left:40px}
.callbox .ic{width:40px;height:40px;border-radius:50%;background:#fff;display:flex;align-items:center;justify-content:center}
.callbox small{display:block;font-size:13px}
.callbox b{font-size:26px}

/* hero */
.hero{top:80px;height:850px;overflow:hidden}
.hero-photo{left:0;top:0;width:1200px;height:850px;background:linear-gradient(160deg,#8fa9bd 0%,#4e6b86 40%,#24405e 70%,#182d48 100%)}
.hero-card{left:80px;top:190px;width:540px;height:360px;background:#fff;padding:50px 40px 0 45px}
.hero-card h1{font-size:56px;line-height:1.02;color:var(--navy);font-weight:700;border-left:6px solid var(--green);padding-left:14px;margin-left:-20px}
.hero-card p{font-size:14px;line-height:1.6;color:var(--muted);margin:22px 0 26px;width:400px}
.hero-wave{left:0;bottom:0}

/* about */
.about{top:930px;height:500px}
.collage{left:100px;top:40px;width:450px;height:330px}
.about-text{left:620px;top:40px;width:480px}
.about-text h2{font-size:42px;line-height:1.2;color:var(--navy);margin:14px 0 18px}
.about-text p{font-size:14px;line-height:1.65;color:var(--muted);margin-bottom:16px}

/* features */
.features{top:1430px;height:400px;background:linear-gradient(#fff 0,#fff 100px,var(--light) 100px)}
.feature-card{left:95px;top:100px;width:1010px;height:220px;background:#fff;border-radius:0 0 30px 30px;box-shadow:0 10px 30px rgba(20,40,80,.08);display:flex;padding:50px 55px;gap:50px}
.feature{flex:1;display:flex;gap:18px}
.feature .ic{flex:0 0 60px;height:60px;border-radius:50%;border:2px solid var(--navy);display:flex;align-items:center;justify-content:center}
.feature h3{font-size:24px;color:var(--navy);line-height:1}
.feature h4{font-size:16px;color:var(--navy);font-weight:400;margin:4px 0 10px}
.feature p{font-size:13px;line-height:1.55;color:var(--muted)}

/* services */
.services{top:1830px;height:670px;background:var(--light)}
.services h2{position:absolute;left:95px;top:50px;font-size:44px;color:var(--navy)}
.arrows{right:95px;top:50px;display:flex;gap:10px}
.arrows span{width:40px;height:40px;background:#fff;border:1px solid var(--line);display:flex;align-items:center;justify-content:center}
.svc{top:145px;width:320px;height:380px}
.svc .img{width:320px;height:180px}
.svc .box{position:absolute;left:0;top:150px;width:295px;height:210px;background:#fff;padding:26px 24px}
.svc .box h3{font-size:22px;color:var(--navy);margin-bottom:12px}
.svc .box p{font-size:13px;line-height:1.6;color:var(--muted);margin-bottom:16px}
.svc .box a{font-size:13px;font-weight:700;color:var(--green);text-decoration:none}
.svc.feature-blue .box{background:var(--navy)}
.svc.feature-blue .box h3,.svc.feature-blue .box p,.svc.feature-blue .box a{color:#fff}
.more{left:500px;top:585px;width:200px;height:48px;border:2px solid var(--green);border-radius:24px;color:var(--green);font-size:13px;font-weight:700;display:flex;align-items:center;justify-content:center;letter-spacing:.5px}

/* projects */
.projects{top:2500px;height:700px}
.center-head{width:1200px;text-align:center;display:flex;flex-direction:column;align-items:center}
.center-head h2{font-size:48px;color:var(--navy);margin-top:14px}
.proj-main{left:215px;top:220px;width:750px;height:405px;border-radius:14px}
.proj-side{top:220px;height:405px;border-radius:14px}
.parrow{top:400px;width:56px;height:56px;background:#fff;border-radius:6px;display:flex;align-items:center;justify-content:center}
.proj-caption{left:260px;top:545px;width:655px;height:60px;display:flex}
.proj-caption .lbl{flex:1;background:var(--green);color:#fff;font-size:22px;font-weight:700;display:flex;align-items:center;padding-left:24px}
.proj-caption .go{width:70px;background:var(--green-dark);display:flex;align-items:center;justify-content:center}

/* testimonials */
.testi{top:3200px;height:560px;background:var(--light)}
.tcard{top:190px;width:310px;height:240px;background:#fff;text-align:center;padding:34px 26px 0}
.tcard .avatar{position:absolute;left:125px;top:-30px;width:60px;height:60px;border-radius:50%;background:linear-gradient(135deg,#9aa7b6,#5a6a7c);border:3px solid #fff}
.stars{color:#f2a33a;font-size:18px;letter-spacing:3px}
.tcard p{font-size:13px;line-height:1.6;color:var(--muted);margin-top:14px}
.tcard .q{position:absolute;left:125px;bottom:-30px;width:60px;height:60px;border-radius:50%;background:var(--green);display:flex;align-items:center;justify-content:center}
.tname{top:466px;width:310px;text-align:center}
.tname b{display:block;font-size:20px;color:var(--ink)}
.tname span{font-size:13px;color:var(--muted)}

/* contact */
.contact{top:3760px;height:640px;overflow:hidden}
.contact-bg{left:0;top:140px;width:1200px;height:500px;background:linear-gradient(180deg,#53677c 0%,#6f7f8e 60%,#8b6f5a 100%)}
.person{left:140px;top:0;width:420px;height:640px;background:linear-gradient(180deg,#c9b39b 0%,#eae6e0 40%,#d9cfc3 100%);border-radius:180px 180px 0 0}
.form{left:650px;top:165px;width:450px;height:475px;background:var(--panel);border:6px solid var(--navy-dark);border-radius:26px 26px 0 0;padding:36px 30px;color:#fff;text-align:center}
.form h2{font-size:30px;font-weight:700;font-family:"Lato",sans-serif}
.form p{font-size:12px;line-height:1.5;opacity:.85;margin:8px 30px 26px}
.field{height:44px;background:rgba(255,255,255,.28);margin-bottom:18px;text-align:left;font-size:10px;letter-spacing:1px;padding:16px 14px;color:#e8eef6}
.field.tall{height:50px}
.form .send{height:48px;background:#fff;border-radius:4px;margin-top:10px}

/* footer */
.footer{top:4400px;height:440px;background:#fff}
.flogo{left:100px;top:140px}
.follow{left:100px;top:205px;display:flex;align-items:center;gap:10px;font-size:13px;font-weight:700;color:var(--ink)}
.follow i{width:26px;height:26px;border-radius:50%;background:var(--navy);display:inline-block}
.fcol{top:70px}
.fcol h4{font-size:15px;color:var(--green);font-weight:700;margin-bottom:22px}
.fcol li{list-style:none;font-size:14px;color:var(--ink);margin-bottom:12px;display:flex;gap:10px;align-items:flex-start}
.fcol li::before{content:"";width:3px}
.fcol.links li{border-bottom:1px solid var(--line);padding-bottom:8px;width:150px}
.nl p{font-size:14px;line-height:1.5;width:230px;margin-bottom:14px}
.nl .row{display:flex;width:250px;border:1px solid var(--line);height:36px}
.nl .row span{flex:1;font-size:12px;color:var(--muted);padding:10px}
.nl .row b{background:var(--green);color:#fff;font-size:11px;padding:11px 10px}
.fbottom{left:100px;top:385px;width:1000px;border-top:1px solid var(--line);text-align:center;padding-top:14px;font-size:13px;color:var(--green);font-weight:700}
</style>
</head>
<body>

<header class="header">
  <div class="abs logo"><i class="dot"></i><span>BrightVX</span></div>
  <div class="abs topbar"><span class="wel">WELCOME</span>
    <span class="mail"><svg width="16" height="12" viewBox="0 0 16 12"><rect x="1" y="1" width="14" height="10" fill="none" stroke="#13305f" stroke-width="1.5"/><path d="M1 1l7 6 7-6" fill="none" stroke="#13305f" stroke-width="1.5"/></svg>info@brightvx.com</span>
  </div>
  <nav class="abs nav"><a class="active">HOME</a><a>About Us</a><a>Services</a><a>Gallery</a><a>Contact Us</a></nav>
  <div class="abs callbox">
    <div class="ic"><svg width="20" height="20" viewBox="0 0 24 24"><path d="M6.6 10.8a15 15 0 006.6 6.6l2.2-2.2a1 1 0 011-.25 11.4 11.4 0 003.6.57 1 1 0 011 1V20a1 1 0 01-1 1A17 17 0 013 4a1 1 0 011-1h3.5a1 1 0 011 1c0 1.25.2 2.45.57 3.57a1 1 0 01-.25 1z" fill="#13305f"/></svg></div>
    <div><small>Call us today at</small><b>(555) 014-2290</b></div>
  </div>
</header>

<section class="hero">
  <div class="abs hero-photo" role="img" aria-label="Technicians installing solar panels on a rooftop under a bright sky"></div>
  <div class="abs hero-card">
    <h1 class="serif">For a sustainable tomorrow</h1>
    <p>Lorem ipsum dolor sit amet, consectetur adipiscing elit, sed do eiusmod tempor incididunt ut labore et dolore magna aliqua.</p>
    <a class="btn">Discover More</a>
  </div>
  <svg class="abs hero-wave" width="1200" height="170" viewBox="0 0 1200 170" preserveAspectRatio="none">
    <path d="M0 60 C300 150 700 150 1200 10 L1200 170 L0 170Z" fill="#fff"/>
    <path d="M0 40 C300 130 700 130 1200 0" fill="none" stroke="#13305f" stroke-width="22"/>
    <path d="M0 62 C300 150 700 148 1200 18" fill="none" stroke="#6cb52d" stroke-width="8"/>
  </svg>
</section>

<section class="about">
  <svg class="abs collage" viewBox="0 0 450 330" role="img" aria-label="Photo collage of workers fitting solar panels on a home">
    <defs>
      <linearGradient id="c1" x1="0" y1="0" x2="1" y2="1"><stop offset="0" stop-color="#b79a7c"/><stop offset="1" stop-color="#5c6f82"/></linearGradient>
      <linearGradient id="c2" x1="0" y1="0" x2="1" y2="1"><stop offset="0" stop-color="#d8a87a"/><stop offset="1" stop-color="#3f5a76"/></linearGradient>
      <linearGradient id="c3" x1="0" y1="0" x2="0" y2="1"><stop offset="0" stop-color="#8aa0b4"/><stop offset="1" stop-color="#26405c"/></linearGradient>
    </defs>
    <path d="M60 0H215V150H0V60A60 60 0 0160 0Z" fill="url(#c1)"/>
    <path d="M230 0H410A40 40 0 01450 40V100H230Z" fill="url(#c2)"/>
    <path d="M115 165H340V330H175A60 60 0 01115 270Z" fill="url(#c3)"/>
    <rect x="350" y="115" width="100" height="215" rx="20" fill="#5d7590"/>
    <circle cx="225" cy="163" r="36" fill="#fff"/>
    <circle cx="225" cy="163" r="29" fill="#13305f"/>
    <path d="M225 148v14M216 155a12 12 0 1018 0" fill="none" stroke="#fff" stroke-width="3" stroke-linecap="round"/>
  </svg>
  <div class="abs about-text">
    <div class="tag">About Us</div>
    <h2 class="serif">Join the solar movement, make a difference</h2>
    <p>Lorem ipsum dolor sit amet, consectetur adipiscing elit, sed do eiusmod tempor incididunt ut labore et dolore magna aliqua. Ut enim ad minim veniam, quis nostrud exercitation ullamco.</p>
    <p>Lorem ipsum dolor sit amet, consectetur adipiscing elit, sed do eiusmod tempor incididunt ut labore et dolore magna aliqua. Ut enim ad minim veniam.</p>
    <a class="btn">Contact Us</a>
  </div>
</section>

<section class="features">
  <div class="abs feature-card">
    <div class="feature">
      <div class="ic"><svg width="30" height="30" viewBox="0 0 30 30"><circle cx="15" cy="15" r="11" fill="none" stroke="#13305f" stroke-width="2"/><circle cx="15" cy="15" r="5" fill="none" stroke="#13305f" stroke-width="2"/></svg></div>
      <div><h3 class="serif">Expertise</h3><h4>Lorem Ipsum</h4><p>Lorem ipsum dolor sit amet, simply dummy text of lam, qui nostrud exe</p></div>
    </div>
    <div class="feature">
      <div class="ic"><svg width="30" height="30" viewBox="0 0 30 30"><circle cx="15" cy="11" r="6" fill="none" stroke="#13305f" stroke-width="2"/><path d="M11 16l-3 10 7-3 7 3-3-10" fill="none" stroke="#13305f" stroke-width="2"/></svg></div>
      <div><h3 class="serif">Professional</h3><h4>Lorem Ipsum</h4><p>Lorem ipsum dolor sit amet, simply dummy text of lam, qui nostrud exe</p></div>
    </div>
    <div class="feature">
      <div class="ic"><svg width="30" height="30" viewBox="0 0 30 30"><circle cx="15" cy="10" r="5" fill="none" stroke="#13305f" stroke-width="2"/><path d="M6 26a9 9 0 0118 0" fill="none" stroke="#13305f" stroke-width="2"/></svg></div>
      <div><h3 class="serif">Experienced</h3><h4>Lorem Ipsum</h4><p>Lorem ipsum dolor sit amet, simply dummy text of lam, qui nostrud exe</p></div>
    </div>
  </div>
</section>

<section class="services">
  <div class="abs tag" style="left:95px;top:28px">Benefits</div>
  <h2 class="serif">Services We Provide</h2>
  <div class="abs arrows">
    <span><svg width="10" height="14" viewBox="0 0 10 14"><path d="M8 1L2 7l6 6" fill="none" stroke="#2b2f36" stroke-width="2"/></svg></span>
    <span><svg width="10" height="14" viewBox="0 0 10 14"><path d="M2 1l6 6-6 6" fill="none" stroke="#2b2f36" stroke-width="2"/></svg></span>
  </div>
  <div class="abs svc" style="left:95px">
    <div class="img" role="img" aria-label="Crew mounting panels on a house roof" style="background:linear-gradient(135deg,#c4a283,#6d7d8c)"></div>
    <div class="box"><h3 class="serif">Panel Installation</h3><p>Lorem ipsum dolor sit amet, consectetur. Lorem ipsum dolor sit am et, consectetur Lorem dolor</p><a>Read More</a></div>
  </div>
  <div class="abs svc feature-blue" style="left:440px">
    <div class="img" role="img" aria-label="Solar array on a roof under blue sky" style="background:linear-gradient(180deg,#7fa3c8,#2f4f73)"></div>
    <div class="box"><h3 class="serif">Site Assessment</h3><p>Lorem ipsum dolor sit amet, con sectetur Lorem ipsum dolor sit am et, consectetur Lorem dolor</p><a>Read More</a></div>
  </div>
  <div class="abs svc" style="left:785px">
    <div class="img" role="img" aria-label="Technician with battery backup unit among greenery" style="background:linear-gradient(135deg,#7e9a5a,#3d5a3a)"></div>
    <div class="box"><h3 class="serif">Battery Backup</h3><p>Lorem ipsum dolor sit amet, con sectetur Lorem ipsum dolor sit am et, consectetur Lorem dolor</p><a>Read More</a></div>
  </div>
  <div class="abs more">MORE SERVICES</div>
</section>

<section class="projects">
  <div class="abs center-head" style="top:45px"><div class="tag center">Our Work</div><h2 class="serif">Latest Projects</h2></div>
  <div class="abs proj-side" style="left:-60px;width:240px;background:linear-gradient(135deg,#d9a06a,#4a5d74)" role="img" aria-label="Solar panels at sunset"></div>
  <div class="abs proj-side" style="left:1000px;width:260px;background:linear-gradient(135deg,#7fa2c4,#2c4763)" role="img" aria-label="Solar field under blue sky"></div>
  <div class="abs proj-main" role="img" aria-label="Completed rooftop solar installation on a tiled roof" style="background:linear-gradient(160deg,#8fb0cf 0%,#2d4a6b 45%,#9a6e52 100%)"></div>
  <div class="abs parrow" style="left:80px"><svg width="12" height="18" viewBox="0 0 12 18"><path d="M10 1L2 9l8 8" fill="none" stroke="#2b2f36" stroke-width="2.5"/></svg></div>
  <div class="abs parrow" style="left:1035px"><svg width="12" height="18" viewBox="0 0 12 18"><path d="M2 1l8 8-8 8" fill="none" stroke="#2b2f36" stroke-width="2.5"/></svg></div>
  <div class="abs proj-caption"><div class="lbl">Project 567 in ABC State</div><div class="go"><svg width="26" height="16" viewBox="0 0 26 16"><path d="M0 8h23M16 1l8 7-8 7" fill="none" stroke="#fff" stroke-width="2.5"/></svg></div></div>
</section>

<section class="testi">
  <div class="abs center-head" style="top:20px"><div class="tag center">Testimonials</div><h2 class="serif" style="font-size:44px">What Clients are Saying</h2></div>
  <div class="abs tcard" style="left:95px"><div class="avatar" role="img" aria-label="Client portrait"></div><div class="stars">★★★★★</div><p>Lorem ipsum dolor sit amet, simply consectetur adipiscing elit, sed do eiusmod tempor ut labore et dolore magna.</p><div class="q"><svg width="24" height="20" viewBox="0 0 24 20"><path d="M2 18V10Q2 3 9 2v4Q6 7 6 10h4v8zM14 18V10q0-7 7-8v4q-3 1-3 4h4v8z" fill="#fff"/></svg></div></div>
  <div class="abs tcard" style="left:445px"><div class="avatar" role="img" aria-label="Client portrait"></div><div class="stars">★★★★★</div><p>Lorem ipsum dolor sit amet, simply consectetur adipiscing elit, sed do eiusmod tempor ut labore et dolore magna.</p><div class="q"><svg width="24" height="20" viewBox="0 0 24 20"><path d="M2 18V10Q2 3 9 2v4Q6 7 6 10h4v8zM14 18V10q0-7 7-8v4q-3 1-3 4h4v8z" fill="#fff"/></svg></div></div>
  <div class="abs tcard" style="left:795px"><div class="avatar" role="img" aria-label="Client portrait"></div><div class="stars">★★★★★</div><p>Lorem ipsum dolor sit amet, simply consectetur adipiscing elit, sed do eiusmod tempor ut labore et dolore magna.</p><div class="q"><svg width="24" height="20" viewBox="0 0 24 20"><path d="M2 18V10Q2 3 9 2v4Q6 7 6 10h4v8zM14 18V10q0-7 7-8v4q-3 1-3 4h4v8z" fill="#fff"/></svg></div></div>
  <div class="abs tname" style="left:95px"><b>Mara Quill</b><span>Los Angeles</span></div>
  <div class="abs tname" style="left:445px"><b>Mara Quill</b><span>Australia</span></div>
  <div class="abs tname" style="left:795px"><b>Mara Quill</b><span>Australia</span></div>
</section>

<section class="contact">
  <div class="abs contact-bg" role="img" aria-label="Solar installation backdrop with evening sky"></div>
  <div class="abs person" role="img" aria-label="Smiling customer holding a tablet, shown as flat colour"></div>
  <div class="abs form">
    <h2>Connect With Us</h2>
    <p>Lorem ipsum dolor sit amet, consectetur adipiscing elit, sed do eiusmod tempor incididunt ut labore et.</p>
    <div class="field">NAME</div>
    <div class="field">E-MAIL</div>
    <div class="field tall">MESSAGE</div>
    <div class="send"></div>
  </div>
</section>

<footer class="footer">
  <div class="abs flogo logo" style="position:absolute"><i class="dot"></i><span>BrightVX</span></div>
  <div class="abs follow">Follow Us <i></i><i></i><i></i></div>
  <div class="abs fcol links" style="left:360px"><h4>Quick Links</h4><ul><li>Home</li><li>About us</li><li>Services</li><li>Contact us</li></ul></div>
  <div class="abs fcol" style="left:585px"><h4>Contact</h4><ul>
    <li><svg width="14" height="16" viewBox="0 0 14 16"><path d="M7 15s5-5 5-9A5 5 0 002 6c0 4 5 9 5 9z" fill="none" stroke="#6cb52d" stroke-width="1.6"/><circle cx="7" cy="6" r="2" fill="#6cb52d"/></svg><span>48 Harlow Lane<br>Suite 2</span></li>
    <li><svg width="14" height="14" viewBox="0 0 24 24"><path d="M6.6 10.8a15 15 0 006.6 6.6l2.2-2.2a1 1 0 011-.25 11.4 11.4 0 003.6.57 1 1 0 011 1V20a1 1 0 01-1 1A17 17 0 013 4a1 1 0 011-1h3.5a1 1 0 011 1c0 1.25.2 2.45.57 3.57a1 1 0 01-.25 1z" fill="#6cb52d"/></svg>1-800-555-0190</li>
    <li><svg width="14" height="12" viewBox="0 0 16 12"><rect x="1" y="1" width="14" height="10" fill="none" stroke="#6cb52d" stroke-width="1.5"/><path d="M1 1l7 6 7-6" fill="none" stroke="#6cb52d" stroke-width="1.5"/></svg>info@brightvx.com</li>
  </ul></div>
  <div class="abs fcol nl" style="left:860px"><h4>Join our Newsletter</h4><p>Sign up for our newsletter to know the latest from us</p><div class="row"><span>Email</span><b>SUBSCRIBE</b></div></div>
  <div class="abs fbottom">BrightVX</div>
</footer>

</body>
</html>
```